Company Website

We require an online clothing store website for construction workwear.
It needs to be easy to read, user friendly, easy to navigate purchasing.
We are after designs incorporating our recently design logo, and colour combinations black white and orange (same as the company logo). Needs to highlight quality, safety and products. Any ideas around highlighting branding are welcome.

Target Market(s)

Construction workers and businesses.

Industry/Entity Type

Construction

Coding

Coded - Design and coding required

Number of Pages Required

5+ page

Colors
EE7325
F08F49
F5BC92
FAE3D3
FDF4ED

Requirements
Must have
• Include all pictures, prices and details of the products we sell. See PDF uploaded to brief.
Nice to have
• Simple access to purchase items. Easy to navigate website layout.

```html
<!DOCTYPE html>
<html lang="en">
<head>
<meta charset="utf-8">
<title>Ironline Workwear</title>
<link href="https://fonts.googleapis.com/css2?family=Poppins:wght@400;500;600;700&display=swap" rel="stylesheet">
<style>
:root{
  --orange:#f25c05;
  --orange-soft:#f08f49;
  --black:#111111;
  --dark:#1f1f1f;
  --grey-band:#ebebeb;
  --text:#222;
  --muted:#555;
  --white:#fff;
}
*{box-sizing:border-box;margin:0;padding:0}
html,body{width:1200px;height:3317px;overflow:hidden}
body{font-family:"Poppins",sans-serif;color:var(--text);background:var(--white);position:relative}
.abs{position:absolute}

/* header */
.header{left:0;top:0;width:1200px;height:124px;background:var(--white)}
.brand{left:77px;top:42px}
.brand-name{font-size:34px;font-weight:700;color:var(--orange);letter-spacing:3px;line-height:1}
.brand-sub{font-size:11px;font-weight:600;letter-spacing:6px;color:var(--black);margin-top:4px;padding-left:80px;position:relative}
.brand-sub:before{content:"";position:absolute;left:0;top:7px;width:72px;height:2px;background:var(--black)}
.nav{left:508px;top:60px;display:flex;gap:33px;font-size:13px;color:#333}
.nav a{text-decoration:none;color:inherit;position:relative}
.nav a.active{color:var(--orange)}
.nav a.active:after{content:"";position:absolute;left:-4px;right:-4px;bottom:-10px;height:2px;background:var(--orange)}
.header-icons{left:1026px;top:54px;display:flex;gap:16px;align-items:center}
.cart-badge{position:absolute;left:22px;top:-6px;width:14px;height:14px;border-radius:50%;background:var(--orange);color:#fff;font-size:9px;text-align:center;line-height:14px}

/* hero */
.hero{left:0;top:124px;width:1200px;height:630px;background:#252525}
.hero-photo{left:0;top:0;width:520px;height:630px;background:linear-gradient(160deg,#3a2a24,#6b8aa8 55%,#c7d4b0)}
.hero-copy{left:536px;top:140px}
.hero-copy .l1{font-size:72px;font-weight:700;color:#fff;line-height:1}
.hero-copy .l2{font-size:92px;font-weight:700;color:var(--orange);line-height:.95;letter-spacing:1px}
.hero-copy .l3{font-size:32px;font-weight:500;color:#fff;margin-top:6px;padding-left:6px}
.btn-outline{left:543px;top:391px;width:189px;height:57px;border:3px solid #fff;color:#fff;font-size:19px;font-weight:600;display:flex;align-items:center;justify-content:center}
.dots{display:flex;gap:4px}
.dots span{width:12px;height:12px;border-radius:50%;background:#888}
.dots span.on{background:#fff}

/* features */
.feature{top:802px;width:253px;height:103px;background:#fff;box-shadow:0 2px 10px rgba(0,0,0,.15);display:flex;align-items:center;padding-left:27px;gap:12px}
.feature-icon{width:57px;height:57px;border-radius:50%;background:var(--orange);flex:none;display:flex;align-items:center;justify-content:center}
.feature h4{font-size:13px;font-weight:600;color:var(--black)}
.feature p{font-size:9.5px;color:var(--muted);line-height:1.4;margin-top:3px}

/* section titles */
.sec-title{font-size:40px;font-weight:700;color:var(--orange);line-height:1}
.sec-sub{font-size:22px;font-weight:500;letter-spacing:6px;color:var(--black);position:relative;padding-left:150px;margin-top:4px}
.sec-sub:before{content:"";position:absolute;left:0;top:14px;width:134px;height:2px;background:var(--black)}
.arrow-btn{top:1008px;width:42px;height:54px;display:flex;align-items:center;justify-content:center}

/* products */
.product{top:1121px;width:232px;height:339px;background:#fff;box-shadow:0 2px 8px rgba(0,0,0,.12);text-align:center}
.product-img{height:183px}
.product h5{font-size:15px;font-weight:500;margin-top:20px}
.product .price{font-size:15px;font-weight:600;margin-top:10px}
.stars{color:#f5b800;font-size:13px;letter-spacing:1px;margin-top:3px}
.btn-small{display:inline-block;background:var(--orange);color:#fff;font-size:11px;font-weight:500;padding:3px 10px;margin-top:10px}
.view-more{left:537px;top:1503px;width:126px;height:49px;border:2px solid var(--orange);color:var(--orange);font-size:13px;display:flex;align-items:center;justify-content:center}

/* uniforms band */
.band{left:0;top:1622px;width:1200px;height:458px;background:var(--grey-band)}
.band-copy{left:100px;top:1718px;width:590px;text-align:center}
.band-copy .c1{font-size:31px;font-weight:600;color:var(--orange)}
.band-copy .c2{font-size:68px;font-weight:700;line-height:1;color:var(--black)}
.band-copy .c3{font-size:92px;font-weight:700;line-height:1;color:var(--black)}
.btn-solid{left:299px;top:1934px;width:193px;height:64px;background:var(--orange);color:#fff;font-size:18px;font-weight:500;display:flex;align-items:center;justify-content:center}
.band-photo{left:756px;top:1545px;width:360px;height:535px;background:linear-gradient(180deg,#2f4fa8 0%,#d7ef2a 35%,#c6dd35 55%,#2a4ba0 75%,#26408a 100%);border-radius:140px 140px 0 0}

/* testimonials */
.testi{left:0;top:2080px;width:1200px;height:518px;background:linear-gradient(90deg,#161616,#2b2b28 50%,#161616)}
.testi-title{left:407px;top:2175px}
.testi-title .sec-sub{color:#fff;padding-left:254px;letter-spacing:7px}
.testi-title .sec-sub:before{background:#fff;width:238px}
.t-card{top:2304px;width:394px;height:170px;padding:26px 30px 0 42px}
.t-card p{font-size:11px;line-height:1.6;width:270px;text-indent:48px;position:relative}
.t-card .quote{position:absolute;left:0;top:-2px;font-size:24px;font-weight:700;text-indent:0;line-height:1}
.t-card h6{font-size:13px;font-weight:600;margin-top:14px}
.t-card .stars{font-size:10px;margin-top:0}
.avatar{width:80px;height:80px;border-radius:50%;border:3px solid #fff;background:linear-gradient(#c9bba8,#6a6a6a)}
.circ-dots{left:564px;top:2524px;display:flex;gap:3px}
.circ-dots span{width:12px;height:12px;border-radius:50%;border:1px solid #ccc}
.circ-dots span.on{background:#fff;border-color:#fff}

/* newsletter */
.news-title{left:0;top:2745px;width:1200px;text-align:center;font-size:44px;font-weight:600;color:var(--black)}
.news-sub{left:0;top:2817px;width:1200px;text-align:center;font-size:14px}
.footer{left:0;top:2880px;width:1200px;height:380px;background:var(--black)}
.news-box{left:233px;top:2880px;width:735px;height:105px;background:#fff}
.news-input{left:314px;top:2866px;width:570px;height:65px;border:1px solid #ddd;border-radius:33px;background:#fff;font-size:13px;color:#777;padding:24px 0 0 36px}
.news-btn{left:710px;top:2866px;width:173px;height:65px;border-radius:33px;background:var(--orange);color:#f5c800;font-size:19px;display:flex;align-items:center;justify-content:center}

/* footer */
.f-brand{left:128px;top:3088px}
.f-brand .brand-name{font-size:31px}
.f-brand .brand-sub{color:#fff}
.f-brand .brand-sub:before{background:#fff}
.social{left:156px;top:3162px;display:flex;gap:8px}
.social span{width:28px;height:28px;background:var(--orange);border-radius:3px}
.f-col{top:3055px}
.f-col h3{font-size:14px;font-weight:600;color:var(--orange);margin-bottom:20px}
.f-col li{list-style:none;color:#fff;font-size:13.5px;margin-bottom:9px;padding-left:22px;position:relative}
.f-col li:before{content:"›";position:absolute;left:0;top:-3px;font-size:17px}
.contact-row{display:flex;gap:18px;align-items:flex-start;color:#fff;font-size:13.5px;line-height:1.15;margin-bottom:18px}
.contact-icon{width:27px;height:27px;background:var(--orange);border-radius:3px;flex:none;display:flex;align-items:center;justify-content:center}
.copy-bar{left:0;top:3260px;width:1200px;height:57px;background:#fff}
.copy-text{left:76px;top:3286px;font-size:12px;color:var(--black)}
.pay{top:3282px;width:30px;height:18px;border-radius:2px}
</style>
</head>
<body>

<header class="abs header">
  <div class="abs brand">
    <div class="brand-name">IRONLINE</div>
    <div class="brand-sub">WORKWEAR</div>
  </div>
  <nav class="abs nav">
    <a class="active" href="#">HOME</a><a href="#">SHOP</a><a href="#">PRODUCTS</a><a href="#">ABOUT US</a><a href="#">FAQ</a><a href="#">CONTACT US</a>
  </nav>
  <div class="abs header-icons">
    <span style="position:relative">
      <svg width="24" height="22" viewBox="0 0 24 22"><path d="M1 2h4l3 12h12l3-9H7" fill="none" stroke="#111" stroke-width="2.5"/><circle cx="10" cy="19" r="2" fill="#111"/><circle cx="19" cy="19" r="2" fill="#111"/></svg>
      <span class="cart-badge">0</span>
    </span>
    <svg width="20" height="22" viewBox="0 0 20 22"><circle cx="10" cy="6" r="5" fill="#111"/><path d="M1 22c0-6 4-9 9-9s9 3 9 9z" fill="#111"/></svg>
    <svg width="20" height="20" viewBox="0 0 20 20"><circle cx="8" cy="8" r="6.5" fill="none" stroke="#111" stroke-width="1.8"/><path d="M13 13l6 6" stroke="#111" stroke-width="1.8"/></svg>
  </div>
</header>

<section class="abs hero">
  <div class="abs hero-photo" role="img" aria-label="Smiling worker in red hard hat and gloves giving a thumbs up"></div>
  <div class="abs hero-copy">
    <div class="l1">HARD WORKING</div>
    <div class="l2">WORKWEAR</div>
    <div class="l3">FOR HARD WORKING PEOPLE</div>
  </div>
  <div class="abs btn-outline">SHOP NOW</div>
  <div class="abs dots" style="left:568px;top:534px"><span class="on"></span><span></span><span></span><span></span></div>
</section>

<div class="abs feature" style="left:75px"><div class="feature-icon"><svg width="28" height="18" viewBox="0 0 28 18"><rect x="1" y="2" width="17" height="11" fill="#fff"/><path d="M18 6h5l4 4v3h-9z" fill="#fff"/><circle cx="7" cy="15" r="2.5" fill="#fff"/><circle cx="22" cy="15" r="2.5" fill="#fff"/></svg></div><div><h4>FREE SHIPPING</h4><p>Lorem ipsum dolor sit amet,<br>consectetur adipiscing elit</p></div></div>
<div class="abs feature" style="left:340px"><div class="feature-icon"><svg width="28" height="18" viewBox="0 0 28 18"><rect x="5" y="2" width="13" height="11" fill="#fff"/><path d="M18 6h5l4 4v3h-9z" fill="#fff"/><circle cx="10" cy="15" r="2.5" fill="#fff"/><circle cx="22" cy="15" r="2.5" fill="#fff"/><path d="M0 5h4M0 9h4" stroke="#fff" stroke-width="1.5"/></svg></div><div><h4>FAST DELIVERY</h4><p>Lorem ipsum dolor sit amet,<br>consectetur adipiscing elit</p></div></div>
<div class="abs feature" style="left:605px"><div class="feature-icon"><svg width="22" height="18" viewBox="0 0 22 18"><path d="M2 6h17M15 2l4 4-4 4M20 12H3M7 8l-4 4 4 4" fill="none" stroke="#fff" stroke-width="2"/></svg></div><div><h4>RETURN &amp; EXCHANGE</h4><p>Lorem ipsum dolor sit amet,<br>consectetur adipiscing elit</p></div></div>
<div class="abs feature" style="left:871px"><div class="feature-icon"><svg width="24" height="24" viewBox="0 0 24 24"><path d="M4 12a8 8 0 0116 0" fill="none" stroke="#fff" stroke-width="2"/><rect x="2" y="11" width="4" height="7" fill="#fff"/><rect x="18" y="11" width="4" height="7" fill="#fff"/><circle cx="12" cy="13" r="4" fill="#fff"/><path d="M5 24c1-4 4-6 7-6s6 2 7 6z" fill="#fff"/></svg></div><div><h4>24/7 SUPPORT</h4><p>Lorem ipsum dolor sit amet,<br>consectetur adipiscing elit</p></div></div>

<div class="abs" style="left:76px;top:1003px">
  <div class="sec-title">OUR PRODUCTS</div>
  <div class="sec-sub">SHOP NOW</div>
</div>
<div class="abs arrow-btn" style="left:1036px;background:#fff;box-shadow:0 1px 6px rgba(0,0,0,.15)"><svg width="10" height="14"><path d="M8 1L2 7l6 6" fill="none" stroke="#333" stroke-width="1.5"/></svg></div>
<div class="abs arrow-btn" style="left:1085px;background:var(--orange)"><svg width="10" height="14"><path d="M2 1l6 6-6 6" fill="none" stroke="#fff" stroke-width="1.5"/></svg></div>

<div class="abs product" style="left:102px"><div class="product-img" role="img" aria-label="Worker in hi-vis orange vest beside clothing rack" style="background:linear-gradient(90deg,#2a2f4a,#f26a2a 60%,#6d4a36)"></div><h5>High Visibility Clothing</h5><div class="price">$400.00</div><div class="stars">★★★★★</div><span class="btn-small">SHOP NOW</span></div>
<div class="abs product" style="left:358px"><div class="product-img" role="img" aria-label="Pair of brown leather protective gloves" style="background:radial-gradient(circle,#a8432a 0,#b85a3e 30%,#e7e7e9 60%)"></div><h5>Protective Gloves</h5><div class="price">$100.00</div><div class="stars">★★★★★</div><span class="btn-small">SHOP NOW</span></div>
<div class="abs product" style="left:611px"><div class="product-img" role="img" aria-label="Worn leather safety boots" style="background:radial-gradient(circle,#4a3a2a 0,#5a4a38 30%,#dcdcdc 60%)"></div><h5>Safety footwear</h5><div class="price">$200.00</div><div class="stars">★★★★★</div><span class="btn-small">SHOP NOW</span></div>
<div class="abs product" style="left:865px"><div class="product-img" role="img" aria-label="Worker in white helmet and yellow ear defenders" style="background:linear-gradient(180deg,#2b6fc0,#8fb0c8 55%,#e8c830)"></div><h5>Protective Helmet</h5><div class="price">$250.00</div><div class="stars">★★★★★</div><span class="btn-small">SHOP NOW</span></div>

<div class="abs view-more">VIEW MORE</div>

<section class="abs band"></section>
<div class="abs band-photo" role="img" aria-label="Worker in hi-vis yellow jacket and blue cap"></div>
<div class="abs band-copy">
  <div class="c1">CUSTOMIZED</div>
  <div class="c2">SAFETY</div>
  <div class="c3">UNIFORMS</div>
</div>
<div class="abs btn-solid">SHOP ONLINE</div>

<section class="abs testi" role="img" aria-label="Dimmed background of construction workers on site"></section>
<div class="abs testi-title">
  <div class="sec-title" style="font-size:41px">OUR TESTIMONILAS</div>
  <div class="sec-sub">REVIEWS</div>
</div>
<div class="abs t-card" style="left:150px;background:#2e2e2e;color:#ddd">
  <p><span class="quote" style="color:var(--orange)">❝</span>Lorem ipsum dolor sit amet, consectetur adipiscing elit. Maece nas ac tellus ac ipsum porta viverra sit amet sed leo. Vivamus eu mauris conval-lis, hendrerit</p>
  <h6 style="color:#fff">Dana Mercer</h6><div class="stars">★★★★★</div>
</div>
<div class="abs avatar" style="left:497px;top:2348px" role="img" aria-label="Customer portrait"></div>
<div class="abs t-card" style="left:656px;background:var(--orange);color:#fff;padding-left:95px">
  <p><span class="quote" style="color:#fff">❝</span>Lorem ipsum dolor sit amet, consectetur adipiscing elit. Maece nas ac tellus ac ipsum porta viverra sit amet sed leo. Vivamus eu mauris conval-lis, hendrerit</p>
  <h6>Marcus Hale</h6><div class="stars" style="color:#ffd400">★★★★★</div>
</div>
<div class="abs avatar" style="left:615px;top:2348px" role="img" aria-label="Customer portrait"></div>
<div class="abs circ-dots"><span></span><span></span><span class="on"></span><span></span><span></span></div>

<div class="abs news-title">Our Newsletter Sign Up</div>
<div class="abs news-sub">Subscribe our newsletter to get the latest collections and updates</div>

<footer class="abs footer"></footer>
<div class="abs news-box"></div>
<div class="abs news-input">Enter Email Address</div>
<div class="abs news-btn">SIGNUP</div>

<div class="abs f-brand">
  <div class="brand-name">IRONLINE</div>
  <div class="brand-sub">WORKWEAR</div>
</div>
<div class="abs social"><span></span><span></span><span></span><span></span></div>

<div class="abs f-col" style="left:451px"><h3>HELP &amp; SUPPORT</h3><ul><li>Shipping &amp; Delivery</li><li>Terms &amp; Conditions</li><li>Privacy Policy</li><li>Returns</li></ul></div>
<div class="abs f-col" style="left:676px"><h3>QUICK LINKS</h3><ul><li>Shop</li><li>Products</li><li>About Us</li><li>FAQ</li><li>Contact Us</li></ul></div>
<div class="abs f-col" style="left:858px"><h3>CONTACT DETAILS</h3>
  <div class="contact-row"><span class="contact-icon"><svg width="14" height="14" viewBox="0 0 14 14"><path d="M3 1l2 3-1.5 1.5a8 8 0 005 5L10 9l3 2-1 2c-6 0-11-5-11-11z" fill="#fff"/></svg></span><div>CALL US<br>0400 555 0137</div></div>
  <div class="contact-row"><span class="contact-icon"><svg width="14" height="10" viewBox="0 0 14 10"><rect width="14" height="10" fill="#fff"/><path d="M0 0l7 6 7-6" fill="none" stroke="#f25c05" stroke-width="1.2"/></svg></span><div>EMAIL US<br>sales@ironlinewear.com</div></div>
  <div class="contact-row"><span class="contact-icon"><svg width="12" height="16" viewBox="0 0 12 16"><path d="M6 0a6 6 0 016 6c0 4-6 10-6 10S0 10 0 6a6 6 0 016-6z" fill="#fff"/><circle cx="6" cy="6" r="2" fill="#f25c05"/></svg></span><div>Address line here dummy<br>Address line here</div></div>
</div>

<div class="abs copy-bar"></div>
<div class="abs copy-text">Copyright ©2024– All Rights Reserved by Company name</div>
<div class="abs pay" style="left:964px;background:#d9e4f2"></div>
<div class="abs pay" style="left:998px;background:#c8ccd6"></div>
<div class="abs pay" style="left:1032px;background:#dfe4f0"></div>
<div class="abs pay" style="left:1066px;background:#6fa6d6"></div>
<div class="abs pay" style="left:1097px;background:#e4e4e4"></div>

</body>
</html>
```